Paint Your Own Pottery Studio needs a Menu Design

I'm about to open my "paint your own pottery" studio on December 14th!! I would like to offer a menu of sorts for customers to peruse when they enter.

A couple of menu ideas are this:

#1: Regular session: purchase bisqueware and studio session @ regular rates ($5 for the first 50 minutes and $2 for each additional hour)

#2: Purchase 10 studio hours, get 2 free + 15% off any bisqueware painted during these sessions

#3: Purchase 5 pieces of bisqueware (full price) and the first 5 hours of studio time, get unlimited subsequent studio hours for those 5 pieces.

I hope to offer anywhere from 6-8 menu items.

The studio is located on what used to be the sun porch of an old farmhouse, the house my grandfather and great-grandfather built 100 years ago. The studio has a glorious view of the York River on the chesapeake bay in Virginia. Please see my website info page for more info (www.fernledgeceramics.com).

The studio itself has an industrial + farmhouse vibe to it with only white and dark grey/blue for colors (the colors in my logo). The shelving that will be displaying the unpainted pottery (bisqueware) uses industrial pipe as supports and the wood shelves themselves are stained a dark espresso color. The studio is in the process of being organized, but I will upload some photos for reference.

Target Market(s)

women: 18-65. I plan to have both ladies nights with wine as well as kids birthday parties. Many people will come to make gifts as well.

Industry/Entity Type

Paint

Font styles to use
Serif

Requirements
Must have
• A vibe that matches the feel of the interior design of the studio. Clean lines, farmhouse with industrial/modern updates.

```html
<!DOCTYPE html>
<html lang="en">
<head>
<meta charset="utf-8">
<title>Fernledge Ceramics Co – Studio Menu</title>
<link href="https://fonts.googleapis.com/css2?family=Crimson+Pro:wght@400;500&family=Libre+Caslon+Text:wght@400&family=Playfair+Display:ital@1&display=swap" rel="stylesheet">
<style>
  :root{
    --paper:#ffffff;
    --dots:#d5dce2;
    --panel:#cbbdb6;
    --brown:#4f2a22;
    --slate:#53565e;
    --ink:#2f2c2b;
    --divider:#8a6c63;
  }
  *{margin:0;padding:0;box-sizing:border-box}
  html,body{width:1200px;height:927px;overflow:hidden;background:var(--paper)}
  .menu{position:relative;width:1200px;height:927px;background:var(--paper);font-family:"Crimson Pro",serif;color:var(--ink)}
  .band{position:absolute;left:0;width:1200px;height:44px;background:var(--dots)}
  .band--top{top:0}
  .band--bottom{bottom:0}
  .events-panel{position:absolute;left:802px;top:0;width:345px;height:927px;background:var(--panel)}

  .brand{position:absolute;left:86px;top:124px;display:flex;align-items:center;gap:9px}
  .brand__mark{width:13px;height:13px;border-radius:50%;background:var(--slate)}
  .brand__name{font-family:"Crimson Pro",serif;font-weight:500;font-size:19px;line-height:23px;color:var(--slate);letter-spacing:1px;text-transform:uppercase}

  .welcome{position:absolute;left:255px;top:82px;font-family:"Libre Caslon Text",serif;font-weight:400;font-size:33px;line-height:40px;color:var(--slate);letter-spacing:-.3px;white-space:nowrap}
  .welcome__sub{position:absolute;left:311px;top:125px;font-family:"Playfair Display",serif;font-style:italic;font-size:27px;line-height:36px;color:var(--brown);white-space:nowrap}
  .rule{position:absolute;left:55px;top:184px;width:718px;height:6px;background:var(--brown)}
  .packages-title{position:absolute;left:55px;width:724px;top:200px;text-align:center;font-family:"Playfair Display",serif;font-style:italic;font-size:24.5px;color:var(--brown)}

  .package{position:absolute;display:flex;align-items:center}
  .package__num{font-family:"Libre Caslon Text",serif;font-size:54px;line-height:1;color:var(--slate);width:72px;flex:none;letter-spacing:-3px}
  .package__text{font-size:20px;line-height:25.5px;color:var(--ink);white-space:nowrap}
  .col-left .package{left:57px}
  .col-right .package{left:429px}

  .divider{position:absolute;left:413px;top:250px;height:504px;width:4px;border-left:3px dotted var(--divider)}

  .special{position:absolute;left:56px;top:774px;width:715px;height:88px;border:1.5px solid var(--brown);border-radius:24px;display:flex;align-items:center}
  .special__label{font-family:"Libre Caslon Text",serif;color:var(--brown);text-align:center;width:160px;line-height:1;flex:none}
  .special__label .month{display:block;font-size:19px;letter-spacing:-.6px}
  .special__label .word{display:block;font-size:25px;margin-top:3px;letter-spacing:-.4px}
  .special__offer{font-family:"Libre Caslon Text",serif;font-size:21px;color:var(--brown);margin-left:2px;white-space:nowrap}

  .events-frame{position:absolute;left:849px;top:80px;width:247px;height:118px;border:1.5px solid var(--brown);display:flex;align-items:center;justify-content:center;text-align:center}
  .events-frame::before,.events-frame::after{content:"";position:absolute;top:54px;width:8px;height:8px;border-radius:50%;background:var(--brown)}
  .events-frame::before{left:-5px}
  .events-frame::after{right:-5px}
  .events-frame h2{font-family:"Libre Caslon Text",serif;font-weight:400;font-size:32px;line-height:40px;color:var(--brown)}
  .event{position:absolute;left:802px;width:345px;top:224px;text-align:center}
  .event__name{font-family:"Playfair Display",serif;font-style:italic;font-size:27px;color:var(--brown);margin-bottom:2px}
  .event__detail{font-size:20px;line-height:25.5px;color:var(--ink)}
</style>
</head>
<body>
<main class="menu">
  <div class="band band--top"></div>
  <div class="band band--bottom"></div>
  <aside class="events-panel"></aside>

  <div class="brand">
    <span class="brand__mark"></span>
    <span class="brand__name">Fernledge<br>Ceramics Co</span>
  </div>

  <h1 class="welcome">WELCOME TO THE STUDIO!</h1>
  <p class="welcome__sub">What would you like to do today?</p>
  <div class="rule"></div>
  <p class="packages-title">Choose from a variety of packages</p>

  <section class="col-left">
    <div class="package" style="top:249px"><span class="package__num">#1</span><p class="package__text">Regular session: purchase<br>bisqueware and studio session<br>@ regular rates ($5 for the first<br>50 minutes and $2 for each<br>additional hour)</p></div>
    <div class="package" style="top:392px"><span class="package__num">#2</span><p class="package__text">Purchase 10 studio hours, get 2<br>free + 15% off any bisqueware<br>painted during these sessions</p></div>
    <div class="package" style="top:485px"><span class="package__num">#3</span><p class="package__text">Purchase 5 pieces of bisqueware<br>(full price) and the first 5 hours<br>of studio time, get unlimited<br>subsequent studio hours for<br>those 5 pieces.</p></div>
    <div class="package" style="top:629px"><span class="package__num">#4</span><p class="package__text">Purchase 5 pieces of bisqueware<br>(full price) and the first 5 hours<br>of studio time, get unlimited<br>subsequent studio hours for<br>those 5 pieces.</p></div>
  </section>

  <div class="divider"></div>

  <section class="col-right">
    <div class="package" style="top:249px"><span class="package__num">#5</span><p class="package__text">Regular session: purchase<br>bisqueware and studio session<br>@ regular rates ($5 for the first<br>50 minutes and $2 for each<br>additional hour)</p></div>
    <div class="package" style="top:392px"><span class="package__num">#6</span><p class="package__text">Purchase 10 studio hours, get 2<br>free + 15% off any bisqueware<br>painted during these sessions</p></div>
    <div class="package" style="top:485px"><span class="package__num">#7</span><p class="package__text">Purchase 5 pieces of bisqueware<br>(full price) and the first 5 hours<br>of studio time, get unlimited<br>subsequent studio hours for<br>those 5 pieces.</p></div>
    <div class="package" style="top:629px"><span class="package__num">#8</span><p class="package__text">Purchase 5 pieces of bisqueware<br>(full price) and the first 5 hours<br>of studio time, get unlimited<br>subsequent studio hours for<br>those 5 pieces.</p></div>
  </section>

  <div class="special">
    <div class="special__label"><span class="month">DECEMBER</span><span class="word">SPECIAL</span></div>
    <p class="special__offer">All Holiday Bisqueware – Buy 2 get the 3rd for 1/2 off!</p>
  </div>

  <div class="events-frame"><h2>UPCOMING<br>EVENTS</h2></div>
  <div class="event">
    <p class="event__name">– Ladies Night –</p>
    <p class="event__detail">January xx, 6-8<br>Grab your girlfriends and book<br>your seats today!</p>
  </div>
</main>
</body>
</html>
```